Copperleaf Keystone Method

We are a wealth advisory firm. We need a design that shows our business is built on seven pillars. These seven pillars support all 85 things. These seven pillars form the foundation of our process. As their lives unfold and their needs evolve, they can’t outgrow our process; they’ll grow into it as critical life events occur and their lives progress.

We have an example of pillars, a figure of 8, and trees—we would like it to be modern, clean, and nature-inspired. If you use pillars, they cannot look 80s or like a law office. I am also attaching a picture of our logo and the landing page of our website for reference to our feel and style.
We want to use the language on the sheet with figure 8 in the final design.

Target Market(s)

families and small business owners with 1 million + of investable assets

Industry/Entity Type

Finance

Font styles to use
Sans Serif

Colors
0054AA
0677BA
7BADD7
CADEEF
E8F1F8
FFC000
F8CF3A
FAE287
FDF2CF
FEFAEE
EE7325
F08F49
F5BC92
FAE3D3
FDF4ED

```html
<!DOCTYPE html>
<html lang="en">
<head>
<meta charset="utf-8">
<title>Copperleaf Keystone Method – Ashgrove Capital</title>
<link href="https://fonts.googleapis.com/css2?family=Montserrat:wght@500;600&family=PT+Serif:wght@700&display=swap" rel="stylesheet">
<style>
  :root {
    --backdrop: #b3b3b3;
    --navy: #0b1f3a;
    --orange: #e2562a;
    --ink: #1c2533;
    --rule: #4a4a4a;
    --leaf-deep: #4f8a26;
    --leaf-mid: #7cb340;
    --leaf-light: #b9d86a;
    --white: #ffffff;
  }
  * { box-sizing: border-box; margin: 0; padding: 0; }
  html, body { width: 800px; height: 1200px; overflow: hidden; }
  body { background: var(--backdrop); position: relative; font-family: "Montserrat", Arial, sans-serif; }

  .method-card {
    position: absolute; left: 20px; top: 308px; width: 760px; height: 584px;
    background: linear-gradient(135deg, #ffffff 0%, #f4f4f4 45%, #ffffff 60%, #f1f1f1 100%);
    box-shadow: 10px 10px 0 rgba(0,0,0,0.12);
  }

  .brand { position: absolute; top: 48px; left: 0; width: 100%; display: flex; justify-content: center; align-items: center; gap: 12px; }
  .brand-dot { width: 34px; height: 34px; border-radius: 50%; background: var(--navy); }
  .brand-name { font-weight: 600; font-size: 26px; letter-spacing: 3px; color: var(--navy); line-height: 1; }

  .headline {
    position: absolute; top: 130px; width: 100%; text-align: center; white-space: nowrap;
    font-family: "PT Serif", Georgia, serif; font-weight: 700; font-size: 38px; letter-spacing: -0.5px; line-height: 1;
  }
  .headline .accent { color: var(--orange); }
  .headline .strong { color: var(--navy); }

  .grove-band {
    position: absolute; left: 0; top: 240px; width: 760px; height: 165px;
    background: linear-gradient(180deg, var(--leaf-light) 0%, var(--leaf-mid) 45%, var(--leaf-deep) 85%, var(--leaf-mid) 100%);
  }

  .pillar { position: absolute; width: 0; height: 0; }
  .pillar-icon {
    position: absolute; left: -27px; top: -27px; width: 54px; height: 54px; border-radius: 50%;
    background: var(--orange); box-shadow: 0 0 0 4px rgba(255,255,255,0.8);
    display: flex; align-items: center; justify-content: center;
  }
  .pillar-icon svg { width: 30px; height: 30px; fill: none; stroke: var(--white); stroke-width: 1.6; stroke-linecap: round; stroke-linejoin: round; }
  .pillar-label {
    position: absolute; left: -80px; width: 160px; text-align: center;
    font-size: 11.5px; font-weight: 500; color: var(--ink); line-height: 1.2; letter-spacing: 0.3px;
  }
  .pillar--top .pillar-label { bottom: 40px; }
  .pillar--bottom .pillar-label { top: 40px; }
  .pillar-tick { position: absolute; left: 0; width: 0; height: 10px; border-left: 1px dashed var(--orange); }
  .pillar--top .pillar-tick { bottom: 28px; }
  .pillar--bottom .pillar-tick { top: 28px; }

  .count-rule { position: absolute; left: 41px; top: 520px; width: 678px; border-top: 1px solid var(--rule); }
  .count-pill {
    position: absolute; left: 206px; top: 496px; width: 348px; height: 48px; border-radius: 24px;
    background: var(--navy); color: var(--white);
    font-family: "PT Serif", Georgia, serif; font-weight: 700; font-size: 30px;
    display: flex; align-items: center; justify-content: center;
  }
</style>
</head>
<body>
  <main class="method-card">
    <header class="brand">
      <span class="brand-dot"></span>
      <span class="brand-name">ASHGROVE CAPITAL</span>
    </header>

    <h1 class="headline"><span class="accent">COPPERLEAF KEYSTONE</span> <span class="strong">METHOD</span></h1>

    <div class="grove-band" role="img" aria-label="Illustration area: a row of green trees linked at their roots by a chain"></div>

    <div class="pillar pillar--top" style="left:77px; top:266px;">
      <span class="pillar-label">WEALTH<br>MANAGEMENT</span><span class="pillar-tick"></span>
      <span class="pillar-icon"><svg viewBox="0 0 30 30"><circle cx="19" cy="9" r="4"/><path d="M19 7v4M9 14V6M6 9l3-3 3 3M4 22h7l5 2 9-5-2-2-6 3h-5"/></svg></span>
    </div>
    <div class="pillar pillar--top" style="left:283px; top:266px;">
      <span class="pillar-label">TAX</span><span class="pillar-tick"></span>
      <span class="pillar-icon"><svg viewBox="0 0 30 30"><path d="M8 4h14v22H8z"/><path d="M12 14l5-5M12 9h.1M17 14h.1M11 19h8M11 22h6"/></svg></span>
    </div>
    <div class="pillar pillar--top" style="left:476px; top:266px;">
      <span class="pillar-label">CASH</span><span class="pillar-tick"></span>
      <span class="pillar-icon"><svg viewBox="0 0 30 30"><path d="M4 10l12-4 10 4-12 4z"/><path d="M4 14l10 4 12-4M4 18l10 4 12-4"/><circle cx="15" cy="10" r="1.5"/></svg></span>
    </div>
    <div class="pillar pillar--top" style="left:676px; top:266px;">
      <span class="pillar-label">VALUE ADDED<br>SERVICE</span><span class="pillar-tick"></span>
      <span class="pillar-icon"><svg viewBox="0 0 30 30"><circle cx="15" cy="15" r="10"/><circle cx="15" cy="15" r="6"/><path d="M12 15l2 2 4-4"/></svg></span>
    </div>

    <div class="pillar pillar--bottom" style="left:176px; top:396px;">
      <span class="pillar-tick"></span><span class="pillar-label">RISK<br>MANAGEMENT</span>
      <span class="pillar-icon"><svg viewBox="0 0 30 30"><path d="M7 6h14v19H7z"/><path d="M11 4h6v4h-6zM10 12h8M10 16h6M10 20h4M22 17l4 8h-8z"/></svg></span>
    </div>
    <div class="pillar pillar--bottom" style="left:376px; top:396px;">
      <span class="pillar-tick"></span><span class="pillar-label">ESTATE</span>
      <span class="pillar-icon"><svg viewBox="0 0 30 30"><path d="M15 14V7M15 10c-3 0-4-2-4-4 3 0 4 2 4 4zM15 9c0-2 2-4 4-4 0 3-2 4-4 4M4 18h6l4 2h4M4 23h10l11-5-2-2-7 3"/></svg></span>
    </div>
    <div class="pillar pillar--bottom" style="left:573px; top:396px;">
      <span class="pillar-tick"></span><span class="pillar-label">PHILANTHROPY</span>
      <span class="pillar-icon"><svg viewBox="0 0 30 30"><circle cx="15" cy="6" r="3"/><circle cx="9" cy="10" r="2.5"/><circle cx="21" cy="10" r="2.5"/><path d="M6 24v-6h6v6zM12 21h8l6-4M18 14h-6"/></svg></span>
    </div>

    <div class="count-rule"></div>
    <div class="count-pill">85 THINGS</div>
  </main>
</body>
</html>
```